Landingpage design

We need a landingpage for a chirpnest add campaign. We sell socks made of bamboo in super quality. Our customers loves us, and we have a 5 heart rating at scorevale.com.

We want to create a add campaign targeted new customers, and the offer is that they can buy 1 pair of bamboo socks as a test, for only 20 DKK (2,7 Euro) including shipment. Our webpage is www.fiblora.dk, landingpage should be built i Pagrune, a wysiwyg editor. based on their template. like:
https://fiblora.pagrune.com/13844-sales-page
https://fiblora.pagrune.com/13696-sales-page
https://fiblora.pagrune.com/13845-sales-page

You don't have to follow the templates 100% if you have better ideas. We have an account for stockmerin, so please get stockphotos from here.

Bamboo socks has a lot of great selling points, you can see a good desciption here:
https://tovelin.com/us/why-bamboo

We expect you to have experience in landingpage design, and expect to end up with 2 landingpages we can splittest on.

This is the first of a number of landingpages we need in the future, so for the right person there will be plenty of more work.

Target Market(s)

Denmark

Industry/Entity Type

E-Commerce

Number of Pages Required

2 page

Colors

Designer to choose colors to be used in the design.

Requirements
Must have
• A great selling page, showing all the great things with bamboo socks. It should be supplied with good packshots from stockmerin.com

```html
<!DOCTYPE html>
<html lang="en">
<head>
<meta charset="utf-8">
<title>Fiblora – Bamboo Socks</title>
<link href="https://fonts.googleapis.com/css2?family=Roboto:wght@300;400;500;700&display=swap" rel="stylesheet">
<style>
:root{
  --green:#38aa80;
  --ink:#3a3a3a;
  --muted:#8a8a8a;
  --light-bg:#f1f1f1;
  --white:#ffffff;
  --promo-bg:#e8f0e5;
  --hero-dark:#3b3835;
}
*{box-sizing:border-box;margin:0;padding:0}
html,body{width:1200px;height:2338px;overflow:hidden}
body{font-family:'Roboto',sans-serif;color:var(--ink);background:var(--white);position:relative}
.site-header{position:absolute;top:0;left:0;width:1200px;height:70px;background:var(--white)}
.brand{position:absolute;left:134px;top:17px;display:flex;align-items:center;gap:10px}
.brand-mark{width:36px;height:36px;border:2px solid #222}
.brand-name{font-size:17px;font-weight:500;color:#222;line-height:1.15}
.brand-tagline{font-size:13px;color:#222;line-height:1.2}
.main-nav a{position:absolute;top:27px;font-size:12.5px;color:#666;text-decoration:none;letter-spacing:.3px}
.main-nav .active{color:#333;border-bottom:1px solid #333;padding-bottom:3px}
.btn{display:flex;align-items:center;justify-content:center;position:absolute;font-size:12.5px;font-weight:500;color:var(--white);text-decoration:none;letter-spacing:.3px}
.btn-primary{background:var(--green)}
.btn-outline{border:1.5px solid var(--white);gap:10px}
.header-cta{left:908px;top:20px;width:158px;height:28px}
.hero{position:absolute;top:70px;left:0;width:1200px;height:491px;background:linear-gradient(100deg,#55504b 0%,#3b3835 45%,#2a2826 70%,#6d6660 100%)}
.hero-title{position:absolute;left:134px;top:102px;font-size:42px;font-weight:500;color:var(--white);line-height:1.22}
.hero-points{position:absolute;left:134px;top:222px;list-style:none}
.hero-points li{font-size:15px;color:var(--white);height:27.5px;display:flex;align-items:center;gap:12px}
.hero-buy{left:134px;top:324px;width:193px;height:34px}
.hero-video{left:346px;top:324px;width:191px;height:34px}
.hero-note{position:absolute;left:134px;top:368px;font-size:11.5px;color:#ddd}
.why{position:absolute;top:561px;left:0;width:1200px;height:587px;background:var(--light-bg)}
.why-title{position:absolute;top:100px;width:100%;text-align:center;font-size:34px;font-weight:400;color:#444}
.why-title span{border-bottom:1.5px solid #555;padding-bottom:2px}
.why-intro{position:absolute;top:158px;width:100%;text-align:center;font-size:15px;line-height:28px;color:var(--muted)}
.benefit{position:absolute;top:269px;width:220px;height:195px;background:var(--white);text-align:center;padding-top:30px}
.benefit svg{display:block;margin:0 auto}
.benefit h3{font-size:19px;font-weight:400;color:#444;margin-top:14px}
.benefit p{font-size:11.5px;color:var(--muted);line-height:17px;margin:10px auto 0;width:180px}
.feature{position:absolute;left:0;width:1200px;height:326px;background:var(--white)}
.feature-photo{position:absolute;top:0;width:600px;height:100%}
.feature-text{position:absolute;top:80px;width:410px}
.feature-text h2{font-size:28px;font-weight:500;color:#444}
.feature-text p{font-size:14.5px;color:var(--muted);line-height:26px;margin-top:16px}
.promo{position:absolute;top:2124px;left:0;width:1200px;height:214px;background:var(--promo-bg)}
.promo-rate{position:absolute;left:132px;top:52px;font-size:86px;font-weight:500;color:var(--green);letter-spacing:-1px;line-height:1}
.promo-text{position:absolute;left:354px;top:78px;font-size:24px;font-weight:500;color:#444;line-height:32px}
.promo-buy{left:872px;top:76px;width:194px;height:35px}
.promo-note{position:absolute;left:872px;width:194px;text-align:right;top:122px;font-size:12px;color:var(--muted)}
</style>
</head>
<body>
<header class="site-header">
  <div class="brand">
    <div class="brand-mark"></div>
    <div>
      <div class="brand-name">Fiblora</div>
      <div class="brand-tagline">Basics i bambus - lige til og enkelt</div>
    </div>
  </div>
  <nav class="main-nav">
    <a class="active" href="#" style="left:485px">HOME</a>
    <a href="#" style="left:566px">WHY BAMBOO</a>
    <a href="#" style="left:696px">ABOUT US</a>
    <a href="#" style="left:800px">REVIEWS</a>
  </nav>
  <a class="btn btn-primary header-cta" href="#">BUY NOW</a>
</header>

<section class="hero" role="img" aria-label="Person relaxing on a sofa wearing black knitted bamboo socks, mug in the background">
  <h1 class="hero-title">Enjoy Your First Pair of Bamboo<br>Socks for Only 20 PKK</h1>
  <ul class="hero-points">
    <li><svg width="14" height="11" viewBox="0 0 14 11"><path d="M1 6l4 4 8-9" fill="none" stroke="#fff" stroke-width="1.6"/></svg>We have been working on textile for more than 10 years</li>
    <li><svg width="14" height="11" viewBox="0 0 14 11"><path d="M1 6l4 4 8-9" fill="none" stroke="#fff" stroke-width="1.6"/></svg>All products meet our high quality standards</li>
    <li><svg width="14" height="11" viewBox="0 0 14 11"><path d="M1 6l4 4 8-9" fill="none" stroke="#fff" stroke-width="1.6"/></svg>Our customers loves us, and we have a 5 stars rating at scorevale.com</li>
  </ul>
  <a class="btn btn-primary hero-buy" href="#">BUY NOW</a>
  <a class="btn btn-outline hero-video" href="#"><svg width="10" height="12" viewBox="0 0 10 12"><path d="M0 0l10 6-10 6z" fill="#fff"/></svg>WATCH VIDEO</a>
  <p class="hero-note">Shipment included</p>
</section>

<section class="why">
  <h2 class="why-title">Why <span>Bamboo</span> Clothing?</h2>
  <p class="why-intro">It was only in 2011 that the Eastmoor University discovered how you can make fabric<br>from bamboo stems. Now bamboo has the potential to become the textile of the future.</p>

  <div class="benefit" style="left:134px">
    <svg width="40" height="36" viewBox="0 0 40 36"><path d="M13 2l-11 6 4 8 5-2v20h18V14l5 2 4-8-11-6c-1 4-4 6-7 6s-6-2-7-6z" fill="none" stroke="#38aa80" stroke-width="2" stroke-linejoin="round"/></svg>
    <h3>Comfortable</h3>
    <p>Bamboo fabric breathes making you comfortable in garments made in this.</p>
  </div>
  <div class="benefit" style="left:372px">
    <svg width="40" height="36" viewBox="0 0 40 36"><circle cx="20" cy="18" r="15" fill="none" stroke="#38aa80" stroke-width="2"/><path d="M13 25c0-9 6-13 14-14-1 9-5 14-14 14zM13 25l8-8" fill="none" stroke="#38aa80" stroke-width="2"/></svg>
    <h3>Eco-friendly</h3>
    <p>Bamboo is a very fast-growing, tropical forest product, which does not require the use of pesticides</p>
  </div>
  <div class="benefit" style="left:609px">
    <svg width="40" height="36" viewBox="0 0 40 36"><path d="M12 4l-8 5 3 7 4-2v19h18V14l4 2 3-7-8-5h-16z" fill="none" stroke="#38aa80" stroke-width="2" stroke-linejoin="round"/><path d="M15 20h10M15 25h10" stroke="#38aa80" stroke-width="2"/></svg>
    <h3>Exquistely soft</h3>
    <p>The moment you wear it next to your skin you will notice the difference between other fabrics.</p>
  </div>
  <div class="benefit" style="left:846px">
    <svg width="40" height="36" viewBox="0 0 40 36"><circle cx="20" cy="5" r="3" fill="none" stroke="#38aa80" stroke-width="2"/><path d="M8 26c0-10 5-17 12-17s12 7 12 17" fill="none" stroke="#38aa80" stroke-width="2"/><rect x="6" y="26" width="28" height="7" fill="none" stroke="#38aa80" stroke-width="2"/><path d="M10 20h20M9 23h22" stroke="#38aa80" stroke-width="1.5"/></svg>
    <h3>Thermo-control</h3>
    <p>Bamboo fabric is warm, thanks to its hollow microfibre, yet is also breathable.</p>
  </div>
</section>

<section class="feature" style="top:1148px">
  <div class="feature-photo" style="left:0;background:linear-gradient(135deg,#6b6b6b,#1c1c1c 55%,#555)" role="img" aria-label="Black bamboo socks lying next to polished black leather shoes on grey carpet"></div>
  <div class="feature-text" style="left:647px">
    <h2>Strong Material</h2>
    <p>Bamboo fabric is lightweight yet strong. The natural processing of verdanel bamboo allows the fibre to remain strong to produce an extremely high quality product. This process gives a material that is very durable.</p>
  </div>
</section>

<section class="feature" style="top:1474px">
  <div class="feature-text" style="left:134px">
    <h2>Completely Clean</h2>
    <p>Bamboo fibers doesnot under go much chemical processing to make the fabric ; so you can easily wear it without causing any allergic irritation to the skin that is more prevalent with heavily processes fabrics.</p>
  </div>
  <div class="feature-photo" style="left:600px;background:linear-gradient(120deg,#efe9e2,#d9cdbf 50%,#a89a8a)" role="img" aria-label="Family relaxing together on a sofa wearing black bamboo socks"></div>
</section>

<section class="feature" style="top:1800px">
  <div class="feature-photo" style="left:0;background:radial-gradient(ellipse at 45% 25%,#e07a2a 0%,#7a3210 25%,#2a1a12 55%,#1a1a1a 100%)" role="img" aria-label="Feet in warm patterned bamboo socks resting in front of a fireplace"></div>
  <div class="feature-text" style="left:647px">
    <h2>Water Absorbent</h2>
    <p>Bamboo fibers are water absobent. So if you live in a humid environment this is the fabric for you. Think of the sweat it will absorb and evaporate out of your body.</p>
  </div>
</section>

<section class="promo">
  <div class="promo-rate">-90%</div>
  <p class="promo-text">Get Your First Pair of Socks With<br>an Exclusive Discount</p>
  <a class="btn btn-primary promo-buy" href="#">BUY NOW</a>
  <p class="promo-note">Shipment included</p>
</section>
</body>
</html>
```